Want a vertical business card using photo to scale with background whited out and in top right corner:Hair BY In bottom left corner:Danita Corvish

Business

Contact information on back of card: Velvet Fern Studio(in large font at the top)In the middle: 1822 Marron rd.Suite#42 Brinmoor Ca.90417(Inside Pivet Salons)Bottom:(right)Appt.space(left)contact info.555 318 2764 dc-corvish@example.net

• Back side:(in larger font at the top the name of the business) Velvet Fern Studio

there are 2 photos of the card I am trying to emulate and a photo of me that I want to use

```html
<!DOCTYPE html>
<html lang="en">
<head>
<meta charset="utf-8">
<title>Hair by Danita Corvish – Business Card</title>
<link rel="stylesheet" href="https://fonts.googleapis.com/css2?family=Questrial&family=Nothing+You+Could+Do&display=swap">
<style>
  :root {
    --page-bg: #e4e2e0;
    --card-white: #ffffff;
    --ink: #111111;
    --accent-pink: #d81b5e;
    --photo-light: #f4f1f2;
    --photo-mid: #5a3a4c;
    --photo-dark: #1c1420;
    --bracket-grey: #cfcfcf;
    --appt-fill: #fbeef3;
    --label-grey: #a8a8a8;
  }
  * { box-sizing: border-box; margin: 0; padding: 0; }
  html, body { width: 1200px; height: 1000px; overflow: hidden; }
  body {
    background: var(--page-bg);
    font-family: "Questrial", Arial, sans-serif;
    color: var(--ink);
    position: relative;
  }
  .card {
    position: absolute;
    top: 110px;
    width: 440px;
    height: 770px;
    background: var(--card-white);
    box-shadow: 0 6px 22px rgba(0,0,0,0.18);
    overflow: hidden;
  }

  /* Front */
  .card--front { left: 130px; }
  .front-photo {
    position: absolute;
    left: 0; right: 0; top: 170px; bottom: 0;
    background: linear-gradient(180deg, var(--card-white) 0%, var(--photo-light) 20%, var(--photo-mid) 55%, var(--photo-dark) 100%);
  }
  .front-title {
    position: absolute;
    top: 48px;
    right: 44px;
    font-size: 58px;
    letter-spacing: 2px;
    font-weight: 400;
  }
  .front-title .by { color: var(--accent-pink); font-size: 50px; margin-left: 6px; }
  .front-name {
    position: absolute;
    left: 38px;
    bottom: 52px;
    font-family: "Nothing You Could Do", cursive;
    font-size: 46px;
    color: #ffffff;
    transform: rotate(-8deg);
    transform-origin: left bottom;
    white-space: nowrap;
  }
  .front-name .surname { color: var(--accent-pink); }

  /* Back */
  .card--back { left: 630px; }
  .studio-name {
    position: absolute;
    top: 44px;
    left: 0; right: 0;
    text-align: center;
    font-weight: 400;
    line-height: 1;
  }
  .studio-name .line-main {
    display: block;
    font-size: 60px;
    letter-spacing: 1px;
    color: var(--ink);
    margin-right: 30px;
  }
  .studio-name .line-sub {
    display: block;
    font-size: 36px;
    color: var(--accent-pink);
    margin-left: 60px;
    margin-top: -2px;
  }
  .address {
    position: absolute;
    top: 178px;
    left: 0; right: 0;
    text-align: center;
    font-style: normal;
    font-weight: 400;
    font-size: 27px;
    line-height: 1.25;
  }
  .address .note { font-size: 22px; }
  .appointment {
    position: absolute;
    top: 348px;
    left: 64px;
    width: 312px;
    height: 232px;
  }
  .appointment svg { position: absolute; inset: 0; }
  .appointment-label {
    position: absolute;
    top: 18px; left: 0; right: 0;
    text-align: center;
    font-size: 14px;
    letter-spacing: 4px;
    color: var(--label-grey);
  }
  .contact {
    position: absolute;
    right: 40px;
    bottom: 48px;
    text-align: right;
  }
  .contact-phone {
    font-size: 27px;
    display: flex;
    align-items: center;
    justify-content: flex-end;
    gap: 10px;
    margin-bottom: 14px;
  }
  .contact-email { font-size: 25px; color: var(--accent-pink); }
</style>
</head>
<body>

<section class="card card--front" aria-label="Card front">
  <div class="front-photo" role="img" aria-label="Photo of the stylist at work with a client, on a white background fading to deep plum"></div>
  <h1 class="front-title">HAIR <span class="by">by</span></h1>
  <p class="front-name">Danita <span class="surname">Corvish</span></p>
</section>

<section class="card card--back" aria-label="Card back">
  <h2 class="studio-name">
    <span class="line-main">VELVET</span>
    <span class="line-sub">Fern Studio</span>
  </h2>
  <address class="address">
    4637 Tamsey Road<br>
    Suite#42<br>
    Brinmoor Ca.90417<br>
    <span class="note">(Inside Pivet Salons)</span>
  </address>

  <div class="appointment">
    <svg width="312" height="232" viewBox="0 0 312 232" aria-hidden="true">
      <defs>
        <linearGradient id="apptFill" x1="0" y1="0" x2="0" y2="1">
          <stop offset="0" stop-color="#fdf4f7"/>
          <stop offset="1" stop-color="var(--appt-fill)"/>
        </linearGradient>
      </defs>
      <rect x="14" y="10" width="284" height="212" fill="url(#apptFill)"/>
      <path d="M44 8 H10 V224 H44" fill="none" stroke="var(--bracket-grey)" stroke-width="14"/>
      <path d="M268 8 H302 V224 H268" fill="none" stroke="var(--bracket-grey)" stroke-width="14"/>
    </svg>
    <p class="appointment-label">NEXT APPOINTMENT</p>
  </div>

  <div class="contact">
    <p class="contact-phone">
      <svg width="24" height="24" viewBox="0 0 24 24" aria-hidden="true">
        <circle cx="12" cy="12" r="10.5" fill="none" stroke="var(--ink)" stroke-width="1.6"/>
        <path d="M9 7.5c-.8.4-1.5 1.4-1 3 .6 2 2.3 4 4.4 5.1 1.4.7 2.5.3 3-.4l-1.6-1.6-1.2.8c-1-.5-2-1.6-2.5-2.6l.8-1.2z" fill="var(--ink)"/>
      </svg>
      555 318 2764
    </p>
    <p class="contact-email">dc-corvish@example.net</p>
  </div>
</section>

</body>
</html>
```